Business Card for IT company

I need a high tech looking business card using our logo. I prefer something clean and modern.

Target Market(s)

Buyers of IT hardware and software, IT Techies who are key influencers

Industry/Entity Type

Business

```html
<!DOCTYPE html>
<html lang="en">
<head>
<meta charset="utf-8">
<title>Novalt Consulting – Business Card</title>
<link rel="stylesheet" href="https://fonts.googleapis.com/css2?family=Montserrat:wght@500;600&family=Arimo:wght@400&display=swap">
<style>
  :root {
    --bg: #ece9e4;
    --card: #ffffff;
    --ink: #3a3a3c;
    --green-dark: #2f9a0c;
    --green-light: #84e000;
    --text-dark: #1c1c1c;
  }
  * { margin: 0; padding: 0; box-sizing: border-box; }
  html, body { width: 1200px; height: 929px; overflow: hidden; }
  body {
    background: var(--bg);
    position: relative;
  }
  .card {
    position: absolute;
    left: 280px;
    width: 640px;
    height: 380px;
    background: var(--card);
    box-shadow: 0 6px 18px rgba(0,0,0,0.18);
    overflow: hidden;
  }
  .card--back { top: 54px; }
  .card--front { top: 494px; }
  .card-art {
    position: absolute;
    inset: 0;
    width: 640px;
    height: 380px;
  }
  .brand-name {
    position: absolute;
    font-family: "Montserrat", sans-serif;
    font-weight: 600;
    color: var(--ink);
    letter-spacing: 1px;
    white-space: nowrap;
  }
  .card--back .brand-name { top: 44px; right: 48px; font-size: 34px; }
  .card--front .brand-name { top: 168px; right: 52px; font-size: 34px; }
  .website {
    position: absolute;
    right: 22px;
    bottom: 26px;
    font-family: "Arimo", sans-serif;
    font-size: 19px;
    color: var(--green-dark);
  }
  .contact {
    position: absolute;
    left: 22px;
    bottom: 14px;
    font-family: "Arimo", sans-serif;
    font-size: 18px;
    line-height: 1.4;
    color: var(--text-dark);
  }
</style>
</head>
<body>
  <section class="card card--back">
    <svg class="card-art" viewBox="0 0 640 380" aria-hidden="true">
      <defs>
        <linearGradient id="back-green" x1="0" y1="0" x2="1" y2="0">
          <stop offset="0" stop-color="var(--green-dark)"/>
          <stop offset="1" stop-color="var(--green-light)"/>
        </linearGradient>
      </defs>
      <line class="brand-rule" x1="360" y1="118" x2="600" y2="100" stroke="url(#back-green)" stroke-width="3"/>
      <circle class="swoosh-ring" cx="230" cy="480" r="235" fill="none" stroke="url(#back-green)" stroke-width="14"/>
      <circle class="swoosh-fill" cx="230" cy="510" r="190" fill="url(#back-green)"/>
    </svg>
    <div class="brand-name">Novalt Consulting</div>
    <div class="website">novaltconsulting.com</div>
  </section>

  <section class="card card--front">
    <svg class="card-art" viewBox="0 0 640 380" aria-hidden="true">
      <defs>
        <linearGradient id="front-green" x1="0" y1="0" x2="1" y2="0">
          <stop offset="0" stop-color="var(--green-dark)"/>
          <stop offset="1" stop-color="var(--green-light)"/>
        </linearGradient>
      </defs>
      <circle class="corner-leaf" cx="10" cy="-10" r="165" fill="url(#front-green)"/>
      <circle class="corner-ring" cx="0" cy="0" r="282" fill="none" stroke="url(#front-green)" stroke-width="14"/>
      <rect class="contact-band" x="0" y="296" width="640" height="84" fill="url(#front-green)"/>
    </svg>
    <div class="brand-name">Novalt Consulting</div>
    <div class="contact">
      <p>Email: novalt@mail.com</p>
      <p>Phone: 2222-3333-4444</p>
    </div>
  </section>
</body>
</html>
```